TIDAL BODY CARE PACKAGING RENDERINGS

Logo and Packaging renderings for 4 core line Body Skin Care products called Tidal Glow. We make unisex natural skin care for the body. We would like designs that are very colorful and eye catching to communicate the humorous personality of the brand but communicate the efficacy and power of our formulations!

Target Market(s)

UNISEX, AGE 18 - 45, DRY SKIN, BLACK PEOPLE, NATURAL, CONSCIOUS CONSUMER

Industry/Entity Type

Cosmetics

Logo Text

TIDAL GLOW

Colors

Designer to choose colors to be used in the design.

Requirements
Must have
• BOLD CLEAR GRAPHICS
• COLOR (DIFFERENT COLORS PER PRODUCT)
Nice to have
• BLACK AND / OR WHITE WITH POPS OF BOLD COLOR
• BOLD COLOR OVERALL
• TYPOGRAPHIC ART STYLE

```html
<!DOCTYPE html>
<html lang="en">
<head>
<meta charset="utf-8">
<title>Tidal Glow – Hand &amp; Body Lotion Range</title>
<link href="https://fonts.googleapis.com/css2?family=Oswald:wght@500;700&family=Roboto+Slab:wght@800&display=swap" rel="stylesheet">
<style>
  :root {
    --bg: #ffffff;
    --tube-black: #222222;
    --cap-grey: #4b4b4b;
    --cap-shade: #3b3b3b;
    --cap-line: #5a5a5a;
    --ink-light: #f2f2f2;
    --ink-muted: #c4c4c4;
    --orange: #f7941d;
    --yellow: #eef03c;
    --green: #6cc136;
    --pink: #ec1c8c;
    --blue: #22a8e0;
  }
  * { box-sizing: border-box; margin: 0; padding: 0; }
  html, body { width: 1200px; height: 900px; overflow: hidden; background: var(--bg); }
  body { font-family: "Oswald", "Arial Narrow", sans-serif; }

  .range {
    width: 1200px; height: 900px;
    display: flex; justify-content: center; align-items: flex-end;
    gap: 18px; padding-bottom: 150px;
  }

  .tube { width: 196px; display: flex; flex-direction: column; align-items: center; }
  .tube--hero {
    transform: translateY(48px) scale(1.13);
    transform-origin: bottom center;
    margin: 0 16px;
    position: relative; z-index: 1;
  }

  .tube-shell {
    width: 100%;
    height: 440px;
    display: flex; flex-direction: column;
    clip-path: polygon(0 0, 100% 0, 93% 100%, 7% 100%);
    background: var(--tube-black);
  }
  .tube-head {
    background: var(--accent);
    height: 135px;
    display: flex; align-items: flex-end; justify-content: center;
    padding-bottom: 16px;
    border-top: 8px solid color-mix(in srgb, var(--accent) 75%, white);
  }
  .brand-name {
    color: var(--ink-light);
    font-weight: 700;
    text-align: center;
    line-height: 0.95;
  }
  .brand-name__top { display: block; font-size: 46px; letter-spacing: 2px; }
  .brand-name__bottom {
    display: block; font-size: 15px; font-weight: 500;
    letter-spacing: 6px; margin-top: 2px; padding-left: 6px;
    color: var(--ink-light);
  }

  .tube-body {
    flex: 1;
    padding: 14px 22px 0 20px;
    color: var(--ink-light);
    display: flex; flex-direction: column;
  }

  .claims { display: grid; grid-template-columns: 13px 11px 1fr; column-gap: 5px; height: 120px; }
  .tagline {
    writing-mode: vertical-rl; transform: rotate(180deg);
    font-size: 9.5px; font-weight: 700; color: var(--accent);
    white-space: nowrap; text-align: center; line-height: 13px;
  }
  .paint-swatch { background: var(--accent); border-radius: 2px; margin: 2px 0; }

  .claim-organic { font-size: 14px; font-weight: 700; line-height: 1.1; white-space: nowrap; }
  .claim-restore { font-size: 23px; font-weight: 700; line-height: 1.05; letter-spacing: 0.5px; }

  .ingredients-row { display: flex; gap: 2px; margin-top: 5px; align-items: stretch; }
  .ingredients { list-style: none; font-size: 12px; font-weight: 700; line-height: 1.18; white-space: nowrap; }
  .vertical-word {
    writing-mode: vertical-rl; transform: rotate(180deg);
    font-size: 10.5px; font-weight: 700; line-height: 12px; text-align: center;
  }
  .cert-badge { width: 21px; height: 22px; background: var(--ink-light); align-self: flex-end; margin-left: 2px; }

  .product-name {
    font-size: 38px; font-weight: 700; color: var(--accent);
    line-height: 1; margin-top: 8px; white-space: nowrap; letter-spacing: 0.5px;
  }
  .benefit { display: flex; align-items: flex-end; gap: 6px; line-height: 1; margin-top: 3px; }
  .benefit__label { font-size: 10.5px; font-weight: 700; line-height: 1.05; white-space: nowrap; }
  .benefit__power { font-size: 26px; font-weight: 700; }

  .format {
    position: relative;
    font-family: "Roboto Slab", Georgia, serif; font-weight: 800;
    color: var(--ink-muted); text-align: center;
    margin: 12px -22px 0 -20px; padding: 2px 0; line-height: 1;
  }
  .format::before, .format::after {
    content: ""; position: absolute; top: 6px; bottom: 2px; width: 22px; background: var(--accent);
  }
  .format::before { left: 0; }
  .format::after { right: 0; }
  .format__top { display: block; font-size: 11px; }
  .format__main { display: block; font-size: 23px; letter-spacing: 0.5px; }
  .fill-weight { font-size: 6.5px; text-align: right; margin-top: 8px; color: var(--ink-muted); }

  .tube-cap {
    width: 76%; height: 72px;
    background: linear-gradient(180deg, var(--cap-shade) 0 8px, var(--cap-grey) 8px 46px, var(--cap-line) 46px 48px, var(--cap-grey) 48px);
    border-radius: 0 0 10px 10px;
  }

  .tube--orange { --accent: var(--orange); }
  .tube--yellow { --accent: var(--yellow); }
  .tube--green  { --accent: var(--green); }
  .tube--pink   { --accent: var(--pink); }
  .tube--blue   { --accent: var(--blue); }
</style>
</head>
<body>
<main class="range">

  <article class="tube tube--orange">
    <div class="tube-shell">
      <header class="tube-head"><h2 class="brand-name"><span class="brand-name__top">TIDAL</span><span class="brand-name__bottom">GLOW</span></h2></header>
      <section class="tube-body">
        <div class="claims">
          <p class="tagline">DRY SKIN DONT LIVE HERE NO MORE</p>
          <div class="paint-swatch" role="img" aria-label="Painted brush stroke in accent colour"></div>
          <div>
            <p class="claim-organic">100% ORGANIC</p>
            <p class="claim-restore">RESTORE</p>
            <div class="ingredients-row">
              <ul class="ingredients"><li>MARULA OIL</li><li>MANGO BUTTER</li><li>KOKUM BUTTER</li></ul>
              <span class="vertical-word">HYDRATE</span>
              <span class="vertical-word">VEGAN</span>
              <span class="cert-badge" role="img" aria-label="Certification badge"></span>
            </div>
          </div>
        </div>
        <p class="product-name">SO LUSH</p>
        <p class="benefit"><span class="benefit__label">ULTIMATE<br>DRY SKIN FIX</span><span class="benefit__power">POWER</span></p>
        <p class="format"><span class="format__top">HAND &amp; BODY</span><span class="format__main">LOTION</span></p>
        <p class="fill-weight">Fill weight: 200ml/6.8 fl oz</p>
      </section>
    </div>
    <div class="tube-cap"></div>
  </article>

  <article class="tube tube--yellow">
    <div class="tube-shell">
      <header class="tube-head"><h2 class="brand-name"><span class="brand-name__top">TIDAL</span><span class="brand-name__bottom">GLOW</span></h2></header>
      <section class="tube-body">
        <div class="claims">
          <p class="tagline">DRY SKIN DONT LIVE HERE NO MORE</p>
          <div class="paint-swatch" role="img" aria-label="Painted brush stroke in accent colour"></div>
          <div>
            <p class="claim-organic">100% ORGANIC</p>
            <p class="claim-restore">RESTORE</p>
            <div class="ingredients-row">
              <ul class="ingredients"><li>MARULA OIL</li><li>MANGO BUTTER</li><li>KOKUM BUTTER</li></ul>
              <span class="vertical-word">HYDRATE</span>
              <span class="vertical-word">VEGAN</span>
              <span class="cert-badge" role="img" aria-label="Certification badge"></span>
            </div>
          </div>
        </div>
        <p class="product-name">SO LUSH</p>
        <p class="benefit"><span class="benefit__label">ULTIMATE<br>DRY SKIN FIX</span><span class="benefit__power">POWER</span></p>
        <p class="format"><span class="format__top">HAND &amp; BODY</span><span class="format__main">LOTION</span></p>
        <p class="fill-weight">Fill weight: 200ml/6.8 fl oz</p>
      </section>
    </div>
    <div class="tube-cap"></div>
  </article>

  <article class="tube tube--green tube--hero">
    <div class="tube-shell">
      <header class="tube-head"><h2 class="brand-name"><span class="brand-name__top">TIDAL</span><span class="brand-name__bottom">GLOW</span></h2></header>
      <section class="tube-body">
        <div class="claims">
          <p class="tagline">DRY SKIN DONT LIVE HERE NO MORE</p>
          <div class="paint-swatch" role="img" aria-label="Painted brush stroke in accent colour"></div>
          <div>
            <p class="claim-organic">100% ORGANIC</p>
            <p class="claim-restore">RESTORE</p>
            <div class="ingredients-row">
              <ul class="ingredients"><li>MARULA OIL</li><li>MANGO BUTTER</li><li>KOKUM BUTTER</li></ul>
              <span class="vertical-word">HYDRATE</span>
              <span class="vertical-word">VEGAN</span>
              <span class="cert-badge" role="img" aria-label="Certification badge"></span>
            </div>
          </div>
        </div>
        <p class="product-name">SO LUSH</p>
        <p class="benefit"><span class="benefit__label">ULTIMATE<br>DRY SKIN FIX</span><span class="benefit__power">POWER</span></p>
        <p class="format"><span class="format__top">HAND &amp; BODY</span><span class="format__main">LOTION</span></p>
        <p class="fill-weight">Fill weight: 200ml/6.8 fl oz</p>
      </section>
    </div>
    <div class="tube-cap"></div>
  </article>

  <article class="tube tube--pink">
    <div class="tube-shell">
      <header class="tube-head"><h2 class="brand-name"><span class="brand-name__top">TIDAL</span><span class="brand-name__bottom">GLOW</span></h2></header>
      <section class="tube-body">
        <div class="claims">
          <p class="tagline">DRY SKIN DONT LIVE HERE NO MORE</p>
          <div class="paint-swatch" role="img" aria-label="Painted brush stroke in accent colour"></div>
          <div>
            <p class="claim-organic">100% ORGANIC</p>
            <p class="claim-restore">RESTORE</p>
            <div class="ingredients-row">
              <ul class="ingredients"><li>MARULA OIL</li><li>MANGO BUTTER</li><li>KOKUM BUTTER</li></ul>
              <span class="vertical-word">HYDRATE</span>
              <span class="vertical-word">VEGAN</span>
              <span class="cert-badge" role="img" aria-label="Certification badge"></span>
            </div>
          </div>
        </div>
        <p class="product-name">SO LUSH</p>
        <p class="benefit"><span class="benefit__label">ULTIMATE<br>DRY SKIN FIX</span><span class="benefit__power">POWER</span></p>
        <p class="format"><span class="format__top">HAND &amp; BODY</span><span class="format__main">LOTION</span></p>
        <p class="fill-weight">Fill weight: 200ml/6.8 fl oz</p>
      </section>
    </div>
    <div class="tube-cap"></div>
  </article>

  <article class="tube tube--blue">
    <div class="tube-shell">
      <header class="tube-head"><h2 class="brand-name"><span class="brand-name__top">TIDAL</span><span class="brand-name__bottom">GLOW</span></h2></header>
      <section class="tube-body">
        <div class="claims">
          <p class="tagline">DRY SKIN DONT LIVE HERE NO MORE</p>
          <div class="paint-swatch" role="img" aria-label="Painted brush stroke in accent colour"></div>
          <div>
            <p class="claim-organic">100% ORGANIC</p>
            <p class="claim-restore">RESTORE</p>
            <div class="ingredients-row">
              <ul class="ingredients"><li>MARULA OIL</li><li>MANGO BUTTER</li><li>KOKUM BUTTER</li></ul>
              <span class="vertical-word">HYDRATE</span>
              <span class="vertical-word">VEGAN</span>
              <span class="cert-badge" role="img" aria-label="Certification badge"></span>
            </div>
          </div>
        </div>
        <p class="product-name">SO LUSH</p>
        <p class="benefit"><span class="benefit__label">ULTIMATE<br>DRY SKIN FIX</span><span class="benefit__power">POWER</span></p>
        <p class="format"><span class="format__top">HAND &amp; BODY</span><span class="format__main">LOTION</span></p>
        <p class="fill-weight">Fill weight: 200ml/6.8 fl oz</p>
      </section>
    </div>
    <div class="tube-cap"></div>
  </article>

</main>
</body>
</html>
```